Chiropractic healthcare group business card

We are a Portland Oregon based chiropractic healthcare group. Looking for a new business card design. Something cutting edge, that shows off our new logo and tag line.Use either of the attached logos.Our tag line = "Feel better and move freely again?"I'm open to about anything, impress me!!
Target Market(s)
Chiropractic patients - Auto injury, back pain, sports injuries, neck , shoulder, hip, knee, ankle pain.
Industry/Entity Type
Chiropractic
Contact Information for Business Card
Dr. Bram Holtvick, D.C.
Clinic name - Fernway Chiropractic
2 clinics
location #1
20418 NW Marwick Road
Suite B
North Plains, OR 97133
Location #2
13529 SE Calloway Street
Portland OR 97236
Main phone line 971.555.0143
website : www.FernwayClinics.example
Tag line "Feel better and move freely again?"
Colors
Designer to choose colors to be used in the design.
Requirements
Must have
- Use the logo colors -- Want the orange color to be a TRUE orange.
- Both clinic address
- phone number
- website
- personal email - b.holtvick@ReliefBeginsHere.example
- tag line - "Feel better and move freely again?"

```html
<!DOCTYPE html>
<html lang="en">
<head>
<meta charset="utf-8">
<title>Fernway Chiropractic – Business Card</title>
<link rel="stylesheet" href="https://fonts.googleapis.com/css2?family=Roboto:wght@400;500;700&display=swap">
<style>
  :root {
    --backdrop: #353535;
    --card: #2c2c2c;
    --card-light: #303030;
    --orange: #f7931e;
    --white: #ffffff;
    --text: #f1f1f1;
    --icon-glyph: #2c2c2c;
  }
  * { margin: 0; padding: 0; box-sizing: border-box; }
  html, body {
    width: 1200px; height: 869px; overflow: hidden;
    background: var(--backdrop);
    font-family: "Roboto", sans-serif;
  }
  .canvas { position: relative; width: 1200px; height: 869px; }
  .card {
    position: absolute; top: 194px; width: 296px; height: 518px;
    background: linear-gradient(180deg, var(--card) 0%, var(--card-light) 60%, var(--card) 100%);
    color: var(--text); text-align: center;
  }
  .card--front { left: 266px; }
  .card--back { left: 637px; }

  .brand { position: absolute; left: 0; right: 0; display: flex; flex-direction: column; align-items: center; }
  .card--front .brand { top: 66px; }
  .card--back .brand { top: 196px; }
  .brand__dot { width: 30px; height: 30px; border-radius: 50%; background: var(--orange); margin-bottom: 14px; }
  .brand__name {
    font-weight: 500; color: var(--white); text-transform: uppercase;
    font-size: 27px; letter-spacing: 8px; line-height: 1.05; padding-left: 8px;
  }
  .brand__name span { display: block; font-size: 14px; letter-spacing: 3.6px; margin-top: 6px; }

  .doctor { position: absolute; top: 240px; left: 0; right: 0; font-size: 18px; font-weight: 500; color: var(--orange); letter-spacing: -0.2px; }
  .doctor__title { color: var(--white); font-weight: 400; }

  .contact { position: absolute; left: 0; right: 0; font-size: 12.5px; line-height: 17.6px; color: var(--text); }
  .icons { position: absolute; left: 0; right: 0; display: flex; justify-content: center; gap: 4px; }
  .icon { width: 15px; height: 15px; display: block; }

  .tagline { position: absolute; top: 446px; left: 0; right: 0; font-size: 14.5px; color: var(--text); }
</style>
</head>
<body>
<div class="canvas">

  <section class="card card--front">
    <div class="brand">
      <div class="brand__dot"></div>
      <div class="brand__name">Fernway<span>Chiropractic</span></div>
    </div>

    <p class="doctor">DR. BRAM HOLTVICK, <span class="doctor__title">D.C.</span></p>

    <div class="icons" style="top:292px;">
      <svg class="icon" viewBox="0 0 16 16" aria-label="Phone">
        <circle cx="8" cy="8" r="8" fill="var(--orange)"/>
        <path d="M5.2 3.8l1.5 1.6-.8 1.2c.6 1.3 1.4 2.1 2.6 2.7l1.2-.8 1.6 1.5-.9 1.6c-3.2-.3-5.7-2.9-6-6.1z" fill="var(--icon-glyph)"/>
      </svg>
      <svg class="icon" viewBox="0 0 16 16" aria-label="Email">
        <circle cx="8" cy="8" r="8" fill="var(--orange)"/>
        <rect x="3.8" y="5" width="8.4" height="6" fill="none" stroke="var(--icon-glyph)" stroke-width="1.1"/>
        <path d="M3.8 5l4.2 3.4L12.2 5M3.8 11l3-2.7M12.2 11l-3-2.7" fill="none" stroke="var(--icon-glyph)" stroke-width="1"/>
      </svg>
      <svg class="icon" viewBox="0 0 16 16" aria-label="Website">
        <circle cx="8" cy="8" r="8" fill="var(--orange)"/>
        <g fill="none" stroke="var(--icon-glyph)" stroke-width="0.9">
          <circle cx="8" cy="8" r="4.5"/>
          <ellipse cx="8" cy="8" rx="2" ry="4.5"/>
          <path d="M3.5 8h9M4.2 5.7h7.6M4.2 10.3h7.6"/>
        </g>
      </svg>
    </div>
    <div class="contact" style="top:311px;">
      <p>971.555.0143</p>
      <p>b.holtvick@ReliefBeginsHere.example</p>
      <p>www.FernwayClinics.example</p>
    </div>

    <div class="icons" style="top:371px;">
      <svg class="icon" viewBox="0 0 16 16" aria-label="Location">
        <circle cx="8" cy="8" r="8" fill="var(--orange)"/>
        <path d="M8 3.4a3 3 0 0 0-3 3c0 2.2 3 5.8 3 5.8s3-3.6 3-5.8a3 3 0 0 0-3-3z" fill="none" stroke="var(--icon-glyph)" stroke-width="1"/>
        <circle cx="8" cy="6.4" r="1" fill="var(--icon-glyph)"/>
      </svg>
    </div>
    <div class="contact" style="top:389px;">
      <p>13529 SE Calloway Street</p>
      <p>Portland OR 97236</p>
    </div>

    <div class="icons" style="top:429px;">
      <svg class="icon" viewBox="0 0 16 16" aria-label="Location">
        <circle cx="8" cy="8" r="8" fill="var(--orange)"/>
        <path d="M8 3.4a3 3 0 0 0-3 3c0 2.2 3 5.8 3 5.8s3-3.6 3-5.8a3 3 0 0 0-3-3z" fill="none" stroke="var(--icon-glyph)" stroke-width="1"/>
        <circle cx="8" cy="6.4" r="1" fill="var(--icon-glyph)"/>
      </svg>
    </div>
    <div class="contact" style="top:447px;">
      <p>20418 NW Marwick Road</p>
      <p>Suite B, North Plains, OR 97133</p>
    </div>
  </section>

  <section class="card card--back">
    <div class="brand">
      <div class="brand__dot"></div>
      <div class="brand__name">Fernway<span>Chiropractic</span></div>
    </div>
    <p class="tagline">Feel better and move freely again</p>
  </section>

</div>
</body>
</html>
```